Postcard for Online Training Company for Real Estate Agents

We need a high-end professionally designed 2 sided color postcard to send out to Real Estate Agents to use our online, on-demand training service. We would like it to look clean and not busy. Our color scheme is Turquoise, Black and Blue. Color scheme can be seen on website address. Our main target audience are people who just entered the real estate profession. Most of them do no get an on-boarding training if they are not with a big company. We provide very low cost, highly professional training. For just $24.99 per month they have access to all the on-demand training of how to be a real estate agent. The real estate exam to get a license only has the laws and not how to be a a real estate agent.

This will also be use for small companies who do have their own training program for new real estate agent employees.

Target Market(s)

New Real Estate Agents

Industry/Entity Type

Real Estate Agent

Font styles to use
Serif
Sans Serif

Colors
33b8a4
0455a3
000000
b2b2b2

Requirements
Must have
• Both Sides Design Requirements:
• Includes Website address
• Includes Logo
• Includes Price of $24.99 per month (in some shape)
• Front needs to have these two sentences:
• “We help Real Estate agents learn how to close more business and make money”
• “On-Boarding for new agents”
• Back needs to have these 4 questions:
• "Just passed the Real Estate exam?"
• “How do I find clients?”
• “What are the steps to selling a home?”
• “How do I open escrow?”
• Website Address:
• HearthwiseSchool.com
• Logo:
• Attached
Should not have
• This should not look like it is trying to sell a house or look like it is from real estate agent

```html
<!DOCTYPE html>
<html lang="en">
<head>
<meta charset="utf-8">
<title>Hearthwise School Postcard</title>
<link href="https://fonts.googleapis.com/css2?family=Open+Sans:wght@600;700&family=Oswald:wght@400;500&display=swap" rel="stylesheet">
<style>
  :root {
    --turquoise: #14a3c4;
    --sky: #1aa9e6;
    --ink: #141414;
    --charcoal: #2b2b2b;
    --silver: #b2b2b2;
    --paper: #ffffff;
    --backdrop: #e9e9e9;
    --light-text: #f2f2f2;
    --muted: #d6d6d6;
  }
  * { margin: 0; padding: 0; box-sizing: border-box; }
  html, body { width: 907px; height: 1200px; overflow: hidden; }
  body {
    background: var(--backdrop);
    position: relative;
    font-family: "Open Sans", Arial, sans-serif;
  }
  .postcard {
    position: absolute;
    left: 120px;
    width: 610px;
    height: 472px;
    background: var(--paper);
    overflow: hidden;
    box-shadow: 0 4px 14px rgba(0,0,0,0.25);
  }
  .postcard--front { top: 87px; }
  .postcard--back { top: 600px; }
  .postcard__art { position: absolute; inset: 0; }
  .abs { position: absolute; }

  .brand-name {
    font-family: "Open Sans", Arial, sans-serif;
    font-weight: 600;
    color: var(--turquoise);
    white-space: nowrap;
    text-align: center;
  }
  .tagline {
    font-weight: 700;
    color: var(--light-text);
    white-space: nowrap;
    text-align: center;
  }
  .tagline em { font-style: normal; color: var(--sky); }

  .price-badge {
    border-radius: 50%;
    background: radial-gradient(circle at 50% 40%, #3cc3f5, var(--sky) 60%, #0c86c4);
    border: 4px solid #bfe9fb;
    box-shadow: 0 0 0 4px var(--sky);
    color: #fff;
    display: flex; flex-direction: column; align-items: center; justify-content: center;
    font-family: "Oswald", Arial, sans-serif;
    line-height: 1;
  }
  .price-badge__amount { font-weight: 500; }
  .price-badge__term { font-family: "Open Sans", Arial, sans-serif; font-weight: 700; }

  /* Front */
  .front__brand { left: 300px; top: 74px; width: 280px; font-size: 27px; }
  .front__tagline { left: 300px; top: 137px; width: 280px; font-size: 16px; }
  .front__promise {
    left: 300px; top: 196px; width: 300px;
    color: #fff; font-weight: 700; font-size: 18.5px; line-height: 33px;
    text-align: center; text-transform: uppercase;
  }
  .front__cta { left: 290px; width: 300px; text-align: center; font-family: "Oswald", Arial, sans-serif; white-space: nowrap; }
  .front__cta--lead { top: 350px; font-size: 17px; color: var(--muted); }
  .front__cta--offer { top: 374px; font-size: 23px; color: var(--sky); }
  .front__url { left: 290px; top: 414px; width: 300px; text-align: center; font-size: 19px; font-weight: 600; color: #fff; }
  .front__badge { left: 18px; top: 332px; width: 120px; height: 120px; }
  .front__badge .price-badge__amount { font-size: 30px; }
  .front__badge .price-badge__term { font-size: 13px; margin-top: 3px; }

  /* Back */
  .back__brand { left: 10px; top: 62px; width: 250px; font-size: 23px; }
  .back__tagline { left: 5px; top: 107px; width: 260px; font-size: 15px; }
  .back__questions {
    list-style: none;
    left: 0; top: 162px; width: 295px;
    color: #fff; font-weight: 600; font-size: 14.5px; line-height: 25.5px;
    text-align: center;
  }
  .back__cta { left: 24px; font-family: "Oswald", Arial, sans-serif; white-space: nowrap; text-transform: uppercase; }
  .back__cta--lead { top: 298px; font-size: 12.5px; color: var(--muted); }
  .back__cta--offer { top: 318px; font-size: 12.5px; line-height: 20px; color: var(--sky); }
  .back__url { left: 24px; top: 362px; font-size: 14px; font-weight: 600; color: #fff; }
  .back__badge { left: 258px; top: 10px; width: 84px; height: 84px; }
  .back__badge .price-badge__amount { font-size: 21px; }
  .back__badge .price-badge__term { font-size: 9px; margin-top: 2px; }
  .stamp-box { left: 509px; top: 25px; width: 85px; height: 62px; border: 1.5px solid var(--silver); }
  .address-line { left: 384px; width: 210px; height: 0; border-top: 1.5px solid var(--silver); }
</style>
</head>
<body>

<section class="postcard postcard--front">
  <svg class="postcard__art" width="610" height="472" viewBox="0 0 610 472">
    <defs>
      <linearGradient id="frontPhotoTone" x1="0" y1="0" x2="1" y2="1">
        <stop offset="0" stop-color="#8a7a5c"/>
        <stop offset="0.5" stop-color="#3a3a3c"/>
        <stop offset="1" stop-color="#1c2030"/>
      </linearGradient>
      <radialGradient id="darkPanel" cx="0.6" cy="0.3" r="0.8">
        <stop offset="0" stop-color="#3a3a3a"/>
        <stop offset="1" stop-color="#0e0e0e"/>
      </radialGradient>
      <linearGradient id="silverEdge" x1="0" y1="0" x2="1" y2="0">
        <stop offset="0" stop-color="#8c8c8c"/>
        <stop offset="0.5" stop-color="#f4f4f4"/>
        <stop offset="1" stop-color="#9a9a9a"/>
      </linearGradient>
    </defs>
    <rect width="610" height="472" fill="url(#frontPhotoTone)" role="img" aria-label="Photo of a smiling young agent in a dark suit and red tie, arms crossed"/>
    <polygon points="262,0 610,0 610,183 290,183" fill="url(#darkPanel)"/>
    <polygon points="246,0 262,0 290,183 276,183" fill="url(#silverEdge)"/>
    <rect x="282" y="183" width="328" height="131" fill="var(--turquoise)"/>
    <rect x="282" y="180" width="328" height="4" fill="url(#silverEdge)"/>
    <rect x="282" y="313" width="328" height="4" fill="url(#silverEdge)"/>
    <polygon points="290,317 610,317 610,472 212,472" fill="url(#darkPanel)"/>
    <polygon points="276,317 290,317 212,472 196,472" fill="url(#silverEdge)"/>
  </svg>

  <div class="abs brand-name front__brand">Hearthwise School</div>
  <div class="abs tagline front__tagline">ON-BOARDING FOR <em>NEW AGENTS</em></div>
  <p class="abs front__promise">We help real estate agents<br>learn how to close more<br>business and make money!</p>
  <div class="abs front__cta front__cta--lead">START MAKING MORE MONEY TODAY</div>
  <div class="abs front__cta front__cta--offer">FOR A FREE COURSE OVERVIEW VISIT</div>
  <div class="abs front__url">HearthwiseSchool.com</div>
  <div class="abs price-badge front__badge">
    <span class="price-badge__amount">$24.99</span>
    <span class="price-badge__term">per month</span>
  </div>
</section>

<section class="postcard postcard--back">
  <svg class="postcard__art" width="610" height="472" viewBox="0 0 610 472">
    <defs>
      <radialGradient id="darkPanelBack" cx="0.5" cy="0.3" r="0.8">
        <stop offset="0" stop-color="#3a3a3a"/>
        <stop offset="1" stop-color="#0e0e0e"/>
      </radialGradient>
      <linearGradient id="agentPhotoTone" x1="0" y1="0" x2="0" y2="1">
        <stop offset="0" stop-color="#b89c82"/>
        <stop offset="0.35" stop-color="#3a3334"/>
        <stop offset="1" stop-color="#1a1a1c"/>
      </linearGradient>
    </defs>
    <rect x="0" y="0" width="288" height="153" fill="url(#darkPanelBack)"/>
    <rect x="0" y="153" width="295" height="127" fill="var(--turquoise)"/>
    <rect x="0" y="283" width="292" height="107" fill="url(#darkPanelBack)"/>
    <rect x="288" y="0" width="4" height="153" fill="var(--silver)"/>
    <rect x="292" y="283" width="4" height="107" fill="var(--silver)"/>
    <path d="M236,244 H270 V290 H303 V390 H185 V290 H236 Z" fill="url(#agentPhotoTone)" role="img" aria-label="Photo of a young agent in a black blazer holding an orange folder"/>
  </svg>

  <div class="abs brand-name back__brand">Hearthwise School</div>
  <div class="abs tagline back__tagline">ON-BOARDING FOR <em>NEW AGENTS</em></div>
  <ul class="abs back__questions">
    <li>Just passed the Real Estate exam?</li>
    <li>How do I find clients?</li>
    <li>What are the steps to selling a home?</li>
    <li>How do I open escrow?</li>
  </ul>
  <div class="abs back__cta back__cta--lead">Start making more money today</div>
  <div class="abs back__cta back__cta--offer">For a free<br>course overview visit</div>
  <div class="abs back__url">HearthwiseSchool.com</div>
  <div class="abs price-badge back__badge">
    <span class="price-badge__amount">$24.99</span>
    <span class="price-badge__term">per month</span>
  </div>

  <div class="abs stamp-box"></div>
  <div class="abs address-line" style="top:200px"></div>
  <div class="abs address-line" style="top:237px"></div>
  <div class="abs address-line" style="top:274px"></div>
</section>

</body>
</html>
```